Price Package PDF - 2 page PDF of stylized price packages for property management firm

Looking for a 2 x A4 page PDF for our two price packages.
I would like this to be in similar style to our website www.harbourlanerentals.com.au
I have attached an example. But would like mine to be a little more stylish and modern, preferably using design similar to our website.
Words and images also attached

Target Market(s)

investment property owners, male and female, aged 30-60

Industry/Entity Type

Real Estate

Font styles to use
Sans Serif

Requirements
Must have
• split two packages onto seperate A4 pages (See example file attached)
• Contact info:
• Website: www.harbourlanerentals.com.au
• email: info@harbourlanerentals.com.au
• Phone: Tom Radley 0417 562 903, Larisa Okonjo 0409 317 648
• Office Address: Suite 7, 12-14 Wattle Parade, Curl Curl NSW 2096
Nice to have
• I would like to use any of the pictures provided or images of modern residential property interior or of Sydney's Northern Beaches.

```html
<!DOCTYPE html>
<html lang="en">
<head>
<meta charset="utf-8">
<title>Harbour Lane Rentals – All Inclusive Package</title>
<link rel="stylesheet" href="https://fonts.googleapis.com/css2?family=Open+Sans:ital,wght@0,400;0,600;0,700;1,700&family=Oswald:wght@500;600&display=swap">
<style>
  :root {
    --teal: #2e9a9f;
    --teal-bright: #3fc3c8;
    --ink: #141517;
    --white: #ffffff;
    --paper: #ffffff;
    --backdrop: #e9eaec;
    --text: #1c1c1c;
  }
  * { box-sizing: border-box; margin: 0; padding: 0; }
  html, body { width: 900px; height: 1200px; overflow: hidden; }
  body { background: var(--backdrop); font-family: "Open Sans", Arial, sans-serif; position: relative; }

  .flyer {
    position: absolute; left: 35px; top: 17px;
    width: 755px; height: 1060px;
    background: var(--paper);
    transform: scale(1.1); transform-origin: 0 0;
    overflow: hidden;
    box-shadow: 0 2px 10px rgba(0,0,0,.15);
  }
  .abs { position: absolute; }

  .hero-photo {
    left: 0; top: 0; width: 755px; height: 475px;
    background: linear-gradient(180deg, #7cc3ec 0%, #b9def2 22%, #d9d6cc 38%, #8c8f86 50%, #4f7a3c 68%, #6e8f4a 82%, #b9b7b0 100%);
  }
  .shapes { left: 0; top: 0; width: 755px; height: 1060px; }

  .brand {
    left: 40px; top: 66px;
    display: flex; align-items: center; gap: 9px;
    font-weight: 700; font-size: 20px; letter-spacing: 0; color: var(--ink);
    white-space: nowrap;
  }
  .brand-mark { width: 12px; height: 12px; background: var(--teal); }

  .call-now {
    left: 547px; top: 27px; width: 137px; height: 35px;
    background: var(--teal); color: var(--white);
    font-family: "Oswald", "Arial Narrow", sans-serif; font-weight: 600;
    font-size: 24px; line-height: 35px; text-align: center; letter-spacing: .5px;
  }
  .contacts {
    right: 20px; top: 66px; text-align: right;
    font-weight: 700; font-size: 15.5px; line-height: 24px; color: var(--ink);
  }

  .package-title {
    left: 0; top: 490px; width: 357px; height: 73px;
    background: var(--ink); color: var(--white);
    font-family: "Oswald", "Arial Narrow", sans-serif; font-weight: 500;
    font-size: 29px; letter-spacing: 1px; padding: 10px 0 0 28px;
  }
  .package-title::after {
    content: ""; position: absolute; left: 30px; top: 57px; width: 292px; height: 2px; background: var(--white);
  }

  .services {
    left: 28px; top: 582px; width: 330px; list-style: none;
    color: var(--white); font-size: 14.2px; line-height: 19.7px;
  }
  .services li { position: relative; padding-left: 12px; }
  .services li::before {
    content: ""; position: absolute; left: 0; top: 8px; width: 4px; height: 4px; border-radius: 50%; background: var(--white);
  }

  .office {
    left: 32px; top: 966px; width: 320px; color: var(--white);
    font-weight: 700; font-size: 13.6px; line-height: 18px;
  }
  .office-row { display: flex; gap: 8px; align-items: flex-start; margin-bottom: 3px; }
  .office-row svg { flex: none; margin-top: 1px; }

  .ring { border-radius: 50%; background: var(--white); box-shadow: 0 0 0 1px rgba(0,0,0,.05); }
  .ring-inner { position: absolute; border-radius: 50%; border: 5px solid var(--ink); }
  .ring-photo { position: absolute; border-radius: 50%; }
  .ring-large { left: 367px; top: 430px; width: 200px; height: 200px; }
  .ring-large .ring-inner { left: 14px; top: 14px; width: 172px; height: 172px; }
  .ring-large .ring-photo { left: 26px; top: 26px; width: 148px; height: 148px;
    background: linear-gradient(180deg, #dbe7ef 0%, #7fb4d6 30%, #3f8fa9 55%, #5fb5b0 75%, #2f8a89 100%); }
  .ring-small { left: 584px; top: 470px; width: 130px; height: 130px; }
  .ring-small .ring-inner { left: 9px; top: 9px; width: 112px; height: 112px; }
  .ring-small .ring-photo { left: 17px; top: 17px; width: 96px; height: 96px;
    background: linear-gradient(180deg, #cfe3ef 0%, #a9c6d6 35%, #b9a48f 55%, #6c97a8 75%, #9fc1c9 100%); }

  .section-tag {
    background: var(--ink); color: var(--teal-bright);
    font-weight: 700; font-style: italic; font-size: 17px; line-height: 31px;
  }
  .about-tag { left: 382px; top: 625px; width: 157px; height: 31px; text-align: center; }
  .about-copy {
    left: 380px; top: 668px; width: 345px;
    font-size: 10.6px; line-height: 13.2px; color: var(--text);
  }
  .fee-tag { left: 382px; top: 816px; width: 210px; height: 31px; padding-left: 13px; }
  .fees {
    left: 380px; top: 858px; width: 340px; list-style: none;
    font-size: 10.6px; line-height: 13.4px; color: var(--text);
  }
  .fees li { position: relative; padding-left: 12px; }
  .fees li::before {
    content: ""; position: absolute; left: 2px; top: 5px; width: 4px; height: 4px; border-radius: 50%; background: var(--teal);
  }

  .website {
    left: 357px; top: 1008px; width: 398px; text-align: center;
    color: var(--teal); font-weight: 600; font-size: 14.5px; letter-spacing: .3px;
  }
</style>
</head>
<body>
<main class="flyer">
  <div class="abs hero-photo" role="img" aria-label="Row of modern terraced townhouses with lush gardens and stairs on a sunny street"></div>

  <svg class="abs shapes" viewBox="0 0 755 1060" aria-hidden="true">
    <polygon points="0,0 447,0 312,133 0,133" fill="#ffffff"/>
    <polygon points="447,0 460,0 324,135 311,135" fill="#141517"/>
    <path d="M357,500 Q560,470 755,560 L755,1060 L357,1060 Z" fill="#ffffff"/>
    <path d="M500,500 Q640,500 755,570" fill="none" stroke="#2e9a9f" stroke-width="4"/>
    <circle cx="705" cy="618" r="2" fill="#3fc3c8"/>
    <circle cx="540" cy="632" r="2" fill="none" stroke="#3fc3c8"/>
    <polygon points="0,470 357,470 357,1000 272,1060 0,1060" fill="#2e9a9f"/>
    <polygon points="357,1000 755,1000 755,1060 272,1060" fill="#141517"/>
  </svg>

  <div class="abs brand"><span class="brand-mark"></span>HARBOUR LANE RENTALS</div>

  <div class="abs call-now">CALL NOW:</div>
  <div class="abs contacts">
    <p>Tom Radley 0417 562 903</p>
    <p>Larisa Okonjo 0409 317 648</p>
  </div>

  <h2 class="abs package-title">All Inclusive Package:</h2>
  <ul class="abs services">
    <li>Securing Tenan</li>
    <li>Reference/Database Checkin</li>
    <li>Lease Preparation and Signing</li>
    <li>Direct Debit rent collection</li>
    <li>Zero arrears policy management</li>
    <li>Payment of Rates and levies</li>
    <li>Insurance management</li>
    <li>Coordination or all repairs and&nbsp;&nbsp;&nbsp; maintenance</li>
    <li>Regular rent reviews and renewals</li>
    <li>Detailed ingoing, ongoing and<br>outgoing inspections with photos and<br>videos – viewable through your<br>personal Landlord portal</li>
    <li>Bond management – lodging and refunding</li>
    <li>Electronic monthly and EOFY statements</li>
    <li>Annual scheduled maintenance report</li>
    <li>Regulation/compliance management</li>
    <li>Tribunal Representation</li>
  </ul>

  <div class="abs office">
    <div class="office-row">
      <svg width="18" height="14" viewBox="0 0 18 14"><rect x="0.5" y="1" width="17" height="12" fill="#141517"/><path d="M1,1.5 L9,8 L17,1.5" fill="none" stroke="#2e9a9f" stroke-width="1.3"/></svg>
      <span>info@harbourlanerentals.com.au</span>
    </div>
    <div class="office-row">
      <svg width="20" height="18" viewBox="0 0 20 18"><path d="M10,1 L19,9 L16.5,9 L16.5,17 L12,17 L12,12 L8,12 L8,17 L3.5,17 L3.5,9 L1,9 Z" fill="#141517"/></svg>
      <span>Office Address: Suite 7, 12-14 Wattle Parade, Curl Curl NSW 2096</span>
    </div>
  </div>

  <div class="abs ring ring-large">
    <div class="ring-inner"></div>
    <div class="ring-photo" role="img" aria-label="Clear turquoise ocean pool with a rocky shoreline"></div>
  </div>
  <div class="abs ring ring-small">
    <div class="ring-inner"></div>
    <div class="ring-photo" role="img" aria-label="Beachfront apartment buildings beside calm water"></div>
  </div>

  <h3 class="abs section-tag about-tag">ABOUT US</h3>
  <div class="abs about-copy">
    <p>Harbour Lane Rentals is a full service agency specializing in property management on Sydney's Northern Beaches.</p>
    <p>We have a strong understanding of the local market, ensuring you get the best tenant, the best return and the highest quality of management and communication.</p>
    <p>Property management is our core business and focus. You will get a professional, senior property manager looking after your property at all times.</p>
    <p>We understand every owner/investor has different needs. Our aim is to personally tailor our services to satisfy those needs and ensure your experience with us is simple easy and confidence inspiring.</p>
  </div>

  <h3 class="abs section-tag fee-tag">All Inclusive Package:</h3>
  <ul class="abs fees">
    <li>Management Rate: 10% + GST of rental income</li>
    <li>Letting Fee: No Charge</li>
    <li>Advertising: No Charge</li>
    <li>Professional Photography: $199 (inc GST) 4 x Photos</li>
    <li>Statements: No Charge</li>
    <li>Lease Preperation: No Charge</li>
    <li>Renewal Fees: No Charge</li>
  </ul>

  <p class="abs website">www.harbourlanerentals.com.au</p>
</main>
</body>
</html>
```